Derya & Kerem Wedding Invitation and Decorative Designs

We are looking for a sweet and elegant design for our wedding invitation. We need different versions of the same design to use both as printed hard copies and in digital formats (WhatsApp image, instagram post, etc) Please see attached sample invitation, which we like as a simple and elegant option, but also find it quite basic. We are open to creative suggestions following a similar style.
Once we decide on an invitation design, we would like to use the same design elements in guest name cards, welcome sign, menu cards and print cover for the dance floor of our wedding venue. Please see random samples of these materials attached. We also attach a photo from our wedding venue displaying a close to final visual of the decoration we chose for our wedding day (sharing in case it helps as an inspiration source and helps with matching decoration colors with the designs)
Requirements
Must have
- Must have a style similar to the attached sample invitation

```html
<!DOCTYPE html>
<html lang="tr">
<head>
<meta charset="utf-8">
<title>Derya &amp; Kerem – Düğün Davetiyesi</title>
<link rel="stylesheet" href="https://fonts.googleapis.com/css2?family=Great+Vibes&family=Tinos:wght@400;700&display=swap">
<style>
  :root {
    --gold: #b89b52;
    --gold-bright: #d9b84a;
    --gold-deep: #c9a43a;
    --bg-lilac: #e9e3f2;
    --bg-pink: #f1dde9;
    --bg-blue: #c9d6e6;
    --bg-cream: #f3efe6;
    --bloom-pink: #d8418f;
    --bloom-magenta: #c85ad0;
    --bloom-purple: #8a3ca8;
    --bloom-green: #5f9444;
    --bloom-yellow: #dcc838;
  }
  * { margin: 0; padding: 0; box-sizing: border-box; }
  html, body { width: 857px; height: 1200px; overflow: hidden; }
  body { background: var(--bg-lilac); }

  .invitation {
    position: relative;
    width: 857px;
    height: 1200px;
    overflow: hidden;
    background:
      radial-gradient(ellipse 380px 300px at 600px 80px, var(--bg-blue), transparent 70%),
      radial-gradient(ellipse 300px 400px at 760px 500px, #d3deeb, transparent 70%),
      radial-gradient(ellipse 420px 360px at 300px 700px, var(--bg-pink), transparent 70%),
      radial-gradient(ellipse 300px 260px at 470px 560px, var(--bg-cream), transparent 70%),
      radial-gradient(ellipse 500px 300px at 420px 1050px, #f0dbe8, transparent 70%),
      linear-gradient(160deg, #e3e4f3, #ecdff0 45%, #e0e2f0);
    color: var(--gold);
    font-family: "Tinos", "Times New Roman", serif;
  }

  .frame { position: absolute; }
  .frame--outer { left: 41px; top: 37px; width: 776px; height: 1124px; border: 1px solid var(--gold-bright); }
  .frame--inner { left: 51px; top: 47px; width: 756px; height: 1104px; border: 3px solid var(--gold-deep); }

  .floral {
    position: absolute;
    top: 258px;
    width: 130px;
    height: 680px;
    background: linear-gradient(180deg,
      var(--bloom-green) 0%,
      var(--bloom-pink) 12%,
      var(--bloom-yellow) 24%,
      var(--bloom-magenta) 36%,
      var(--bloom-pink) 50%,
      var(--bloom-purple) 62%,
      var(--bloom-yellow) 73%,
      var(--bloom-pink) 86%,
      var(--bloom-green) 100%);
    -webkit-mask-image: linear-gradient(90deg, #000 35%, transparent), linear-gradient(180deg, transparent, #000 6%, #000 94%, transparent);
    -webkit-mask-composite: source-in;
    mask-image: linear-gradient(90deg, #000 35%, transparent), linear-gradient(180deg, transparent, #000 6%, #000 94%, transparent);
    mask-composite: intersect;
    opacity: .8;
  }
  .floral--left { left: 0; }
  .floral--right { right: 0; transform: scaleX(-1); }

  .block { position: absolute; left: 0; width: 857px; text-align: center; }

  .greeting {
    top: 113px;
    font-size: 29px;
    line-height: 36px;
    letter-spacing: .18em;
  }
  .greeting__strong {
    display: block;
    font-weight: 700;
    font-size: 37px;
    letter-spacing: .03em;
    line-height: 40px;
    margin-top: 3px;
  }

  .couple {
    font-family: "Great Vibes", cursive;
    font-weight: 400;
    line-height: 1;
  }
  .couple__name--first { top: 318px; font-size: 120px; }
  .couple__amp { top: 478px; font-size: 110px; }
  .couple__name--second { top: 588px; font-size: 120px; }

  .venue { top: 710px; }
  .venue__name { font-weight: 700; font-size: 35px; letter-spacing: .14em; line-height: 44px; }
  .venue__address { font-size: 28px; letter-spacing: .14em; line-height: 34px; }

  .date {
    top: 840px;
    font-weight: 700;
    font-size: 39px;
    letter-spacing: .02em;
  }

  .schedule { position: absolute; top: 955px; left: 0; width: 857px; height: 140px; }
  .schedule__item { position: absolute; width: 120px; text-align: center; }
  .schedule__icon { display: block; margin: 0 auto; height: 88px; }
  .schedule__time { display: block; font-size: 30px; line-height: 34px; margin-top: 10px; }
  .schedule__item--drinks { left: 146px; }
  .schedule__item--ceremony { left: 291px; }
  .schedule__item--dinner { left: 453px; }
  .schedule__item--party { left: 612px; }
  .schedule__infinity { display: block; margin: 14px auto 0; }
</style>
</head>
<body>
<main class="invitation">
  <div class="frame frame--outer"></div>
  <div class="frame frame--inner"></div>

  <div class="floral floral--left" role="img" aria-label="Watercolour bouquet of pink roses, purple anemones and yellow flowers with green leaves"></div>
  <div class="floral floral--right" role="img" aria-label="Watercolour bouquet of pink roses, purple anemones and yellow flowers with green leaves"></div>

  <p class="block greeting">
    BU MUTLU GÜNÜMÜZDE<br>
    SIZLERI DE ARAMIZDA<br>
    GÖRMEKTEN MUTLULUK<br>
    DUYACAĞIZ, DÜĞÜNÜMÜZE
    <span class="greeting__strong">DAVETLISINIZ</span>
  </p>

  <h1 class="block couple couple__name--first">Derya</h1>
  <p class="block couple couple__amp">&amp;</p>
  <h1 class="block couple couple__name--second">Kerem</h1>

  <div class="block venue">
    <p class="venue__name">LAVANTA KORU</p>
    <p class="venue__address">KORUYOLU, LALE SOK. NO:18<br>BEYKOZ, ISTANBUL</p>
  </div>

  <p class="block date">24TH AĞUSTOS, 2024</p>

  <section class="schedule">
    <div class="schedule__item schedule__item--drinks">
      <svg class="schedule__icon" viewBox="0 0 60 88" width="60" aria-label="Karşılama kokteyli">
        <path d="M18 4 H42 L40 34 Q30 44 20 34 Z" fill="var(--gold)"/>
        <rect x="28.5" y="40" width="3" height="38" fill="var(--gold)"/>
        <ellipse cx="30" cy="80" rx="12" ry="3" fill="var(--gold)"/>
      </svg>
      <span class="schedule__time">18:00</span>
    </div>
    <div class="schedule__item schedule__item--ceremony">
      <svg class="schedule__icon" viewBox="0 0 90 88" width="90" aria-label="Nikah töreni">
        <g fill="none" stroke="var(--gold)" stroke-width="2">
          <circle cx="32" cy="56" r="23"/>
          <circle cx="58" cy="56" r="23"/>
          <path d="M50 26 L54 21 H62 L66 26 L58 33 Z"/>
          <path d="M58 4 V12 M44 10 L48 15 M72 10 L68 15 M40 22 H46 M70 22 H76"/>
        </g>
      </svg>
      <span class="schedule__time">19:00</span>
    </div>
    <div class="schedule__item schedule__item--dinner">
      <svg class="schedule__icon" viewBox="0 0 70 88" width="70" aria-label="Akşam yemeği">
        <g fill="none" stroke="var(--gold)" stroke-width="2">
          <path d="M10 4 V18 Q10 26 18 28 L52 84 L56 82 L24 26 Q28 22 26 14 L24 4 M15 4 V18 M20 4 V18"/>
          <ellipse cx="52" cy="18" rx="10" ry="15" transform="rotate(30 52 18)"/>
          <path d="M44 30 L14 84 L18 86 L48 32"/>
        </g>
      </svg>
      <span class="schedule__time">20:00</span>
    </div>
    <div class="schedule__item schedule__item--party">
      <svg class="schedule__icon" viewBox="0 0 100 88" width="100" aria-label="Eğlence">
        <g fill="none" stroke="var(--gold)" stroke-width="1.8" stroke-linecap="round">
          <path d="M4 80 Q20 70 30 76 Q40 82 50 70"/>
          <path d="M24 40 Q34 30 30 20 Q28 12 38 8"/>
          <path d="M56 14 Q50 34 60 44 Q70 52 64 66"/>
          <path d="M70 30 Q80 36 88 30"/>
          <path d="M36 56 Q44 50 52 56"/>
        </g>
        <g fill="var(--gold)">
          <rect x="48" y="2" width="4" height="7"/>
          <rect x="84" y="58" width="5" height="6"/>
          <rect x="12" y="54" width="4" height="6"/>
          <rect x="74" y="74" width="5" height="5"/>
          <circle cx="40" cy="44" r="2"/>
          <circle cx="78" cy="14" r="2"/>
        </g>
      </svg>
      <svg class="schedule__infinity" viewBox="0 0 48 22" width="46" height="22" aria-label="Sabaha kadar">
        <path d="M24 11 C18 2 5 2 5 11 C5 20 18 20 24 11 C30 2 43 2 43 11 C43 20 30 20 24 11 Z" fill="none" stroke="var(--gold)" stroke-width="4.5"/>
      </svg>
    </div>
  </section>
</main>
</body>
</html>
```